Dubai Family protection infographic

We need to produce a way of attracting people to a life insurance and critical illness cover seminar. As this is a pretty dull subject for most people, so we need a cool way of getting people to read the invite/marketing collateral.

We're thinking some kind of colourful and attractive infographic that we can use on flyers and posters as well as online and as an emailer.

Content for the graphic is as bellow:

How much does it cost to replace Mum & Dad?

Mum = Chauffer, Cook, Laundry Service, Household Cleaner, Psychologist, Money Manager

Mums typically work a 94-hour week. At a rather paltry $12 per hour, that’s $4,888 per month – or $58,656 each year. (Source: paywell.net)

Dad : The average Western Expat’s salary in the Gulf is $12,215 per month. That’s $146,580 each year. (Source: Harbor Ledger).

Did you know that the average age of critical illness claimants in the Middle East last year was just 48. Of these, 44% were for cancer while 41% were heart related.

The average age of a death claimant was just 50 years old.
(Source: Lindqvist Mutual Assurance)

1 in 3 people will develop some form of cancer during their lifetime.

That’s 2.36 billion people globally.

And that’s equivalent to the population of China, USA, Brazil, Russia, Philippines, France, UK, South Africa and Italy combined.

Does your family have the resources to hand to cope if a tragedy happens to you?

What can you do to protect them and yourself?

Come to the UAE’s first national protection seminar to find out. Join us at Palmcrest Memorial Sports Ground on June 19th at 19:00.

To pre-register, visit www.brightvane.com/events or alternatively register on the door.

```html
<!DOCTYPE html>
<html lang="en">
<head>
<meta charset="utf-8">
<title>How much does it cost to replace Mum &amp; Dad?</title>
<link href="https://fonts.googleapis.com/css2?family=Source+Sans+3:wght@400;600;700;800&display=swap" rel="stylesheet">
<style>
:root{
  --page:#e4e1dc;
  --poster:#2f2f2f;
  --pill:#4a4a4a;
  --rule:#404040;
  --white:#ffffff;
  --soft:#c9c9c9;
  --muted:#8d8d8d;
  --green:#6a9a5a;
  --red:#c2383a;
  --blue:#3ea7d8;
  --orange:#e9a12f;
  --brown:#6b4a2c;
  --flame:#e2522a;
}
*{margin:0;padding:0;box-sizing:border-box}
html,body{width:1200px;height:900px;overflow:hidden;background:var(--page)}
body{font-family:"Source Sans 3",sans-serif;color:var(--white);position:relative}
.poster{position:absolute;left:297px;top:21px;width:550px;height:780px;background:var(--poster);transform:scale(1.1);transform-origin:0 0;box-shadow:0 4px 14px rgba(0,0,0,.35)}
.poster > *{position:absolute}
.title{left:13px;top:4px;font-size:37px;font-weight:800;letter-spacing:-.5px;line-height:1}
.subtitle{left:13px;top:42px;font-size:27px;font-weight:600;color:var(--soft);line-height:1}
.title-icons{left:322px;top:44px}
.brand{left:432px;top:38px;display:flex;align-items:center;gap:6px;font-size:13px;font-weight:700;color:var(--white)}
.brand-mark{width:14px;height:14px;background:var(--blue)}
.pill{background:var(--pill);border-radius:14px;font-size:13px;display:flex;align-items:center;padding:0 10px;height:24px;white-space:nowrap}
.tag{height:24px;font-size:14px;display:flex;align-items:center;padding:0 7px;color:var(--white);white-space:nowrap}
.g{background:var(--green)}.r{background:var(--red)}.b{background:var(--blue)}.o{background:var(--orange)}
.avatar{width:24px;height:24px;border-radius:50%;display:inline-block;margin:0 10px 0 -10px}
.value{border-radius:18px;font-weight:700;display:flex;align-items:center;justify-content:center;white-space:nowrap}
.label{font-size:13px;color:var(--white);white-space:nowrap}
.source{font-size:10px;color:var(--muted);white-space:nowrap}
.box{background:var(--pill);font-size:12.5px;line-height:1.15;padding:4px 8px;white-space:nowrap}
.rule{left:0;width:550px;height:1px;background:var(--rule)}
.circle{border-radius:50%;display:flex;align-items:center;justify-content:center;font-weight:700}
.flat{background:#4f5358}
.cta{left:14px;width:526px;font-size:25px;font-weight:700;line-height:1.05;letter-spacing:-.3px}
.cta small{font-size:19px}
.register{left:14px;top:690px;font-size:19.5px;font-weight:700;color:var(--blue);line-height:1.1;white-space:nowrap}
.funds{left:14px;top:742px;font-size:15px;font-weight:700;color:var(--flame);white-space:nowrap}
.campaign{left:337px;top:732px;width:200px;height:32px;background:var(--white);border:3px solid var(--flame);color:var(--flame);font-size:20px;font-weight:800;display:flex;align-items:center;justify-content:center}
.band{left:0;top:588px;width:550px;height:6px;background:repeating-linear-gradient(135deg,#3a3a3a 0 3px,#2f2f2f 3px 6px)}
</style>
</head>
<body>
<main class="poster">
  <h1 class="title">How much does it cost</h1>
  <p class="subtitle">to replace Mum &amp; Dad?</p>
  <div class="title-icons" role="img" aria-label="Man, dollar sign and woman icons">
    <svg width="50" height="26"><rect x="2" y="2" width="8" height="22" fill="#3ea7d8"/><text x="16" y="22" font-size="22" font-weight="800" fill="#fff" font-family="Source Sans 3,sans-serif">$</text><rect x="36" y="2" width="9" height="22" fill="#c2383a"/></svg>
  </div>
  <div class="brand"><span class="brand-mark"></span>BRIGHTVANE</div>

  <div class="pill" style="left:14px;top:108px;width:92px"><span class="avatar r"></span>Mum</div>
  <div class="pill" style="left:115px;top:108px;width:40px;justify-content:center;font-size:20px;font-weight:700">=</div>
  <div class="tag g" style="left:165px;top:108px">Chauffer</div>
  <div class="tag r" style="left:246px;top:108px">Cook</div>
  <div class="tag b" style="left:300px;top:108px">Laundry service</div>
  <div class="tag o" style="left:427px;top:108px">Psychologist</div>
  <div class="pill" style="left:14px;top:142px;width:140px;font-size:12.5px">Typically works a</div>
  <div class="tag r" style="left:167px;top:141px">Household Cleaner</div>
  <div class="tag g" style="left:310px;top:141px">Money Manager</div>

  <div class="circle" style="left:30px;top:172px;width:72px;height:72px;background:var(--orange);flex-direction:column;line-height:.9"><span style="font-size:24px">94 Hr</span><span style="font-size:13px;font-weight:600">week</span></div>
  <p class="source" style="left:125px;top:178px">(Source: paywell.net)</p>
  <div class="box" style="left:104px;top:200px">At a rather paltry<br>$12 per hour</div>
  <p class="label" style="left:238px;top:180px">That’s</p>
  <div class="value b" style="left:277px;top:173px;width:86px;height:30px;font-size:20px">$4,888</div>
  <p class="label" style="left:370px;top:180px">per month</p>
  <p class="label" style="left:233px;top:222px">Or</p>
  <div class="value r" style="left:255px;top:211px;width:118px;height:36px;font-size:25px">$58,656</div>
  <p class="label" style="left:380px;top:222px">per year</p>
  <div class="rule" style="top:254px"></div>

  <div class="box" style="left:14px;top:268px">The average Western Expat’s<br>salary in the Gulf is ...</div>
  <p class="source" style="left:20px;top:314px">(Source: Harbor Ledger)</p>
  <div class="value o" style="left:205px;top:264px;width:86px;height:26px;font-size:19px">$12,215</div>
  <p class="label" style="left:297px;top:269px">per month</p>
  <p class="label" style="left:212px;top:310px">Or</p>
  <div class="value r" style="left:232px;top:298px;width:140px;height:36px;font-size:25px">$146,580</div>
  <p class="label" style="left:378px;top:310px">per year</p>
  <div class="pill" style="left:434px;top:265px;width:100px"><span class="avatar b"></span>Dad</div>
  <div class="rule" style="top:346px"></div>

  <p style="left:14px;top:350px;font-size:12.5px;line-height:1.15;width:180px"><span style="color:var(--orange);font-weight:700">Did you know</span> that the average age of critical illness claiments in the Middle East last year was</p>
  <div class="circle" style="left:194px;top:355px;width:40px;height:40px;background:var(--red);font-size:22px">48</div>
  <svg style="left:250px;top:356px" width="40" height="40" role="img" aria-label="41 percent donut chart"><circle cx="20" cy="20" r="14" fill="none" stroke="var(--brown)" stroke-width="8"/><circle cx="20" cy="20" r="14" fill="none" stroke="var(--orange)" stroke-width="8" stroke-dasharray="36 88" transform="rotate(-90 20 20)"/><text x="20" y="23" font-size="8" fill="#fff" text-anchor="middle" font-family="Source Sans 3,sans-serif">41%</text></svg>
  <div class="box" style="left:305px;top:358px">Were for<br>Cancer</div>
  <svg style="left:385px;top:356px" width="40" height="40" role="img" aria-label="44 percent donut chart"><circle cx="20" cy="20" r="14" fill="none" stroke="#4a3236" stroke-width="8"/><circle cx="20" cy="20" r="14" fill="none" stroke="var(--red)" stroke-width="8" stroke-dasharray="39 88" transform="rotate(-90 20 20)"/><text x="20" y="23" font-size="8" fill="#fff" text-anchor="middle" font-family="Source Sans 3,sans-serif">44%</text></svg>
  <div class="box" style="left:440px;top:358px">Were heart<br>related</div>
  <p class="source" style="left:442px;top:396px;line-height:1.1">(Source: Lindqvist<br>Mutual Assurance)</p>
  <div class="box" style="left:14px;top:406px;font-size:13px">The average age of a death claimant was just</div>
  <div class="circle" style="left:298px;top:399px;width:38px;height:38px;background:var(--blue);font-size:21px">50</div>
  <div class="box" style="left:340px;top:406px;font-size:13px">years old.</div>
  <div class="rule" style="top:432px"></div>

  <div class="circle" style="left:18px;top:446px;width:24px;height:24px;background:var(--red);font-size:15px">1</div>
  <p class="label" style="left:48px;top:450px">in 3 people</p>
  <div style="left:138px;top:442px;display:flex;gap:6px" role="img" aria-label="Three person icons, one highlighted">
    <span style="width:10px;height:30px;background:var(--soft)"></span><span style="width:10px;height:30px;background:var(--soft)"></span><span style="width:10px;height:30px;background:var(--red)"></span>
  </div>
  <p class="label" style="left:20px;top:478px;line-height:1.15">will develop some form of cancer<br>during their lifetime</p>
  <div class="flat" style="left:205px;top:440px;width:168px;height:84px;border-radius:4px" role="img" aria-label="World map highlighting the listed countries"></div>
  <div class="circle" style="left:370px;top:418px;width:72px;height:72px;background:var(--blue);font-size:27px">2.3</div>
  <p style="left:448px;top:434px;font-size:20px;font-weight:600;line-height:1">billion</p>
  <p class="label" style="left:448px;top:452px">people globally</p>
  <p style="left:373px;top:472px;width:166px;font-size:9px;line-height:1.15;color:var(--soft)">And that’s the equivalent to the population of China, USA, Brazil, Russia, Phillippines, France, UK, South Africa and Italy <b style="color:#fff">combined.</b></p>
  <div class="rule" style="top:527px"></div>

  <div class="box" style="left:14px;top:534px;color:var(--blue);font-size:13px;padding:6px 8px">Does your family have the resources to<br>hand to cope if a tradgedy happens to you?</div>
  <div class="flat" style="left:286px;top:535px;width:66px;height:46px;border-radius:3px" role="img" aria-label="Family of four figures"></div>
  <div class="box" style="left:375px;top:536px;font-size:13px;padding:6px 8px"><span style="color:var(--blue)">What can you do</span> to<br>protect them and yourself?</div>

  <div class="band"></div>
  <p class="cta" style="top:604px">Come to the UAE’s first national protection<br>seminar to find out. <small>Join us at Palmcrest Memorial Sports Ground on June 19th at 19:00</small></p>
  <p class="register">To pre-register, visit www.brightvane.com/events<br>or alternatively register on the door.</p>
  <p class="funds">Raising funds for the Tom Ellery campaign:</p>
  <div class="campaign">ROLL ON AGAIN</div>
</main>
</body>
</html>
```